Business Card Design Project

We need a business card design for a relatively new company called Lumen Stride. We design paddle (an outdoor winter sport primarily played in the midwest and east coast) and tennis bags for women and men. Lumen Stride is a lifestyle brand for the next generation country club goers. Our bags merge fashion with functionality and are making country club sports trendier and more fashionable.

I would like to include space for
Name: (will fill this in for employees)
Lumen Stride
Phone: (will do this)
Email:
www.lumenstride-example.net

Would also like to include Facebook and Twitter icons.
Please do not use pictures of the bags - this is just to give you an idea of what style bags we sell.

Target Market(s)

30 to 40 year old men and women - luxury market

Industry/Entity Type

Fashion

Requirements
Must have
• Would like the company logo included

```html
<!DOCTYPE html>
<html lang="en">
<head>
<meta charset="utf-8">
<title>Lumen Stride – Business Card</title>
<link href="https://fonts.googleapis.com/css2?family=Questrial&display=swap" rel="stylesheet">
<style>
  :root {
    --charcoal: #333333;
    --paper: #ffffff;
    --silver: #bcbcbc;
    --icon-grey: #a9a9a9;
    --ink: #3a3a3a;
  }
  html, body {
    margin: 0;
    padding: 0;
    overflow: hidden;
    background: var(--paper);
  }
  .card {
    position: relative;
    width: 1200px;
    height: 719px;
    overflow: hidden;
    background: var(--paper);
    font-family: "Questrial", "Century Gothic", sans-serif;
  }
  .top-band {
    position: absolute;
    left: 0;
    top: 0;
    width: 1200px;
    height: 478px;
    background: var(--charcoal);
  }
  .contact-list {
    position: absolute;
    left: 52px;
    top: 112px;
    margin: 0;
    padding: 0;
    list-style: none;
    color: var(--paper);
    font-size: 35px;
    line-height: 54px;
  }
  .social-links {
    position: absolute;
    right: 22px;
    top: 117px;
    display: flex;
    gap: 20px;
  }
  .social-links span {
    display: block;
    width: 36px;
    height: 36px;
    background: var(--icon-grey);
    border-radius: 3px;
  }
  .checker {
    position: absolute;
    left: 0;
    top: 0;
  }
  .brand {
    position: absolute;
    left: 58px;
    top: 545px;
    display: flex;
    align-items: center;
    gap: 30px;
    color: var(--ink);
  }
  .brand-mark {
    width: 76px;
    height: 76px;
    border-radius: 50%;
    background: var(--ink);
  }
  .brand-name {
    margin: 0;
    font-size: 76px;
    font-weight: 400;
    line-height: 1;
  }
  .brand-url {
    margin: 4px 0 0 6px;
    font-size: 38px;
    line-height: 1;
  }
</style>
</head>
<body>
  <div class="card">
    <div class="top-band"></div>

    <ul class="contact-list">
      <li>Name</li>
      <li>Lumen Stride</li>
      <li>Phone</li>
      <li>Email</li>
    </ul>

    <div class="social-links" aria-label="Social profiles">
      <span aria-label="Social profile one"></span>
      <span aria-label="Social profile two"></span>
    </div>

    <svg class="checker" width="1200" height="719" viewBox="0 0 1200 719" aria-hidden="true">
      <rect x="1130" y="275" width="70" height="68" fill="var(--silver)"/>
      <rect x="1060" y="343" width="70" height="68" fill="var(--paper)"/>
      <rect x="1130" y="411" width="70" height="67" fill="var(--silver)"/>
      <rect x="985" y="478" width="75" height="68" fill="var(--charcoal)"/>
      <rect x="1130" y="478" width="70" height="68" fill="var(--charcoal)"/>
      <rect x="1060" y="546" width="70" height="70" fill="var(--charcoal)"/>
      <rect x="1130" y="616" width="70" height="68" fill="var(--charcoal)"/>
    </svg>

    <div class="brand">
      <div class="brand-mark" aria-hidden="true"></div>
      <div>
        <p class="brand-name">Lumen Stride</p>
        <p class="brand-url">www.lumenstride-example.net</p>
      </div>
    </div>
  </div>
</body>
</html>
```